Parades of Glint stationary design

Parades of Glint (www.paradesofglint.example) is a company that operates events that display the worlds most exotic cars, motorcyles, aircraft, watercraft and luxury brands. we are cutting edge and are looking for a clean , modern stationary design. our sponsors of the events include names like Vantorro, Molvecci, Castelvandri, Kelmayr, Ravelli, Lun vorel, Quastmere and many other big names. we currently operate in florida but are looking to get into new York and California. I added the logo and two car images.car images are optional and not mandatory for the design. Just thought we would add to see what happens.

Target Market(s)

high end , clean design think KELMAYR DESGN style sharp, clean, cutting edge must appeal to the high end luxury brand corporate companies and car, motorcycle, boat, aircraft and luxury brand collectors

Industry/Entity Type

Events

Font styles to use
Sans Serif

Requirements
Must have
• our contact information
• Neil Horvath
• President
• 352-555-0174
• www.paradesofglint.example
• PO Box 4862
• Dunmore, FL 32000
• for business card my email is neil@paradesofglint.example

```html
<!DOCTYPE html>
<html lang="en">
<head>
<meta charset="utf-8">
<title>Parades of Glint — Stationery</title>
<link rel="stylesheet" href="https://fonts.googleapis.com/css2?family=Arimo:wght@400;700&family=Montserrat:wght@500;600&display=swap">
<style>
  :root{
    --bg:#f2f2f2;
    --paper:#ffffff;
    --edge:#e2e2e2;
    --grey:#9ea6a5;
    --red:#c0141b;
    --ink:#4a4a4a;
    --white:#ffffff;
  }
  *{box-sizing:border-box;margin:0;padding:0}
  html,body{width:1200px;height:937px;overflow:hidden}
  body{background:var(--bg);position:relative;font-family:"Arimo",Arial,sans-serif;color:var(--ink)}
  .sheet{position:absolute;background:var(--paper);border:1px solid var(--edge);overflow:hidden}
  .wave{position:absolute;inset:0;width:100%;height:100%}
  .wave .band-grey{fill:var(--grey)}
  .wave .band-red{fill:var(--red)}
  .brand-name{font-family:"Montserrat",Arial,sans-serif;font-weight:600;color:var(--grey);white-space:nowrap;letter-spacing:.02em;position:absolute}
  .site{position:absolute;font-family:"Montserrat",Arial,sans-serif;font-weight:500;color:var(--white);letter-spacing:.22em;white-space:nowrap}

  /* letterhead */
  .letterhead{left:184px;top:66px;width:388px;height:546px}
  .letterhead .brand-name{left:44px;top:62px;font-size:16px}
  .letter{position:absolute;left:37px;top:139px;width:300px;font-size:5.2px;line-height:7.4px}
  .letter p{margin-bottom:6px}
  .letter .gap{margin-bottom:18px}
  .signature{width:30px;height:14px;background:#e4e4e4;margin:10px 0 8px}
  .letter strong{font-weight:700}
  .letter-contact{position:absolute;right:20px;top:463px;text-align:right;font-size:5.2px;line-height:9px;color:var(--white)}

  /* folder */
  .folder{left:633px;top:40px;width:461px;height:576px}
  .folder .brand-name{left:0;right:0;top:300px;text-align:center;font-size:32px}
  .folder .site{right:18px;top:553px;font-size:11px}

  /* business cards */
  .card{width:177px;height:100px;border-radius:7px}
  .card-front{left:45px;top:658px}
  .card-front .brand-name{left:9px;top:22px;font-size:10px}
  .card-person{position:absolute;right:8px;top:8px;text-align:right}
  .card-person .name{font-size:6px;font-weight:700;color:var(--red);letter-spacing:.03em}
  .card-person .role{font-size:4.5px;color:var(--ink)}
  .card-contact{position:absolute;right:8px;top:50px;text-align:right;font-size:4.2px;line-height:6.2px;color:var(--white)}
  .card-back{left:45px;top:785px}
  .card-back .brand-name{left:0;right:0;top:42px;text-align:center;font-size:12px}

  /* envelopes */
  .envelope{width:435px;height:208px}
  .envelope-front{left:264px;top:672px}
  .envelope-front .brand-name{left:16px;top:30px;font-size:15px}
  .envelope-front .site{right:16px;top:184px;font-size:8px}
  .envelope-back{left:736px;top:672px;width:433px}
  .flap{position:absolute;left:0;top:0;width:100%;height:76px;background:var(--grey);border-radius:0 0 28px 28px}
  .envelope-back .site{left:0;right:0;top:28px;text-align:center;font-size:11px}
</style>
</head>
<body>

<section class="sheet letterhead">
  <svg class="wave" viewBox="0 0 388 546" preserveAspectRatio="none" aria-hidden="true">
    <path class="band-red" d="M0,500 C110,478 240,425 388,432 L388,445 C240,440 110,495 0,516Z"/>
    <path class="band-red" d="M0,519 C120,500 240,450 388,450 L388,453 C240,455 120,506 0,523Z"/>
    <path class="band-grey" d="M0,526 C110,506 230,458 388,456 L388,546 L0,546Z"/>
  </svg>
  <div class="brand-name">Parades of Glint</div>
  <div class="letter">
    <p>July 2, 2012</p>
    <p><strong>Dear CH,</strong><br>Nol Building, Fen St., Country Name</p>
    <p>is simply dummy text of the printing and typesetting industry. Lorem Ipsum has been the industry's standard dummy text ever since the 1500s, when an unknown printer took a galley of type and scrambled it to make a type specimen book. It has survived not only five centuries, but also the leap into electronic typesetting, remaining essentially unchanged. It was popularised in the 1960s with the release of Letraset sheets containing Lorem Ipsum passages, and more recently with desktop publishing software including versions of Lorem Ipsum.</p>
    <p class="gap">is simply dummy text of the printing and typesetting industry. Lorem Ipsum has been the industry's standard dummy text ever since the 1500s, when an unknown printer took a galley of type and scrambled it to make</p>
    <p>is simply dummy text of the printing and typesetting industry. Lorem Ipsum has been the industry's standard dummy text ever since the 1500s, when an unknown printer took a galley of type and scrambled it to make a type specimen book. It has survived not only five centuries, but also the leap into electronic typesetting, remaining essentially unchanged. It was popularised in the 1960s with the release of Letraset sheets containing Lorem Ipsum passages, and more recently with desktop publishing software including versions of Lorem Ipsum.</p>
    <p>Best Regards,</p>
    <div class="signature" role="img" aria-label="Handwritten signature"></div>
    <p><strong>Dalia Brenn</strong><br>Director<br><br>Nol Building, Fen St., Country Name</p>
  </div>
  <div class="letter-contact">
    <strong>PO Box 4862</strong><br>
    <strong>Dunmore, FL 32000</strong><br>
    352-555-0174<br>
    352-555-0174<br>
    352-555-0174<br>
    neil@paradesofglint.example<br>
    www.paradesofglint.example
  </div>
</section>

<section class="sheet folder">
  <svg class="wave" viewBox="0 0 461 576" preserveAspectRatio="none" aria-hidden="true">
    <path class="band-red" d="M0,516 C80,520 220,420 461,405 L461,425 C240,440 90,545 0,548Z"/>
    <path class="band-grey" d="M0,556 C90,560 220,462 461,437 L461,576 L0,576Z"/>
  </svg>
  <div class="brand-name">Parades of Glint</div>
  <div class="site">www.paradesofglint.example</div>
</section>

<section class="sheet card card-front">
  <svg class="wave" viewBox="0 0 177 100" preserveAspectRatio="none" aria-hidden="true">
    <path class="band-red" d="M0,66 C60,60 110,35 177,30 L177,38 C110,44 60,70 0,74Z"/>
    <path class="band-grey" d="M0,78 C60,70 110,47 177,42 L177,100 L0,100Z"/>
  </svg>
  <div class="brand-name">Parades of Glint</div>
  <div class="card-person">
    <div class="name">NEIL HORVATH</div>
    <div class="role">President</div>
  </div>
  <div class="card-contact">
    PO Box 4862<br>
    Dunmore, FL 32000<br>
    352-555-0174<br>
    neil@paradesofglint.example<br>
    www.paradesofglint.example
  </div>
</section>

<section class="sheet card card-back">
  <div class="brand-name">Parades of Glint</div>
</section>

<section class="sheet envelope envelope-front">
  <svg class="wave" viewBox="0 0 435 208" preserveAspectRatio="none" aria-hidden="true">
    <path class="band-red" d="M0,157 C140,150 290,85 435,82 L435,96 C290,100 140,168 0,172Z"/>
    <path class="band-grey" d="M0,182 C150,170 290,110 435,104 L435,208 L0,208Z"/>
  </svg>
  <div class="brand-name">Parades of Glint</div>
  <div class="site">www.paradesofglint.example</div>
</section>

<section class="sheet envelope envelope-back">
  <div class="flap"></div>
  <div class="site">www.paradesofglint.example</div>
</section>

</body>
</html>
```